Open sky balance Business cards - yoga studio

We need business cards for our yoga studio Openbreath Harmony.
We would like to see designs that include the colour blue and our logo.
The business card should communicate a feeling of strength and calm

Business

Requirements
Must have
• The business card must include
"Maren Tollefsen - Director"
and
"42 Quillfern Avenue
Dunmorrow
QLD 4518
Ph - 0451 628 904"

```html
<!DOCTYPE html>
<html lang="en">
<head>
<meta charset="utf-8">
<title>Openbreath Harmony – Business Card</title>
<link rel="stylesheet" href="https://fonts.googleapis.com/css2?family=Arimo:wght@400;700&display=swap">
<style>
  :root {
    --sky: #6db6cd;
    --mist: #dce9f0;
    --paper: #ffffff;
    --page: #ffffff;
    --shadow: rgba(0, 0, 0, 0.28);
  }
  html, body {
    margin: 0;
    padding: 0;
    width: 1200px;
    height: 1000px;
    overflow: hidden;
    background: var(--page);
    font-family: "Arimo", Arial, sans-serif;
  }
  .canvas {
    position: relative;
    width: 1200px;
    height: 1000px;
  }
  .card {
    position: absolute;
    left: 226px;
    width: 745px;
    height: 459px;
    box-shadow: 3px 4px 6px var(--shadow);
    overflow: hidden;
  }
  .card--front {
    top: 20px;
    background: var(--sky);
  }
  .card--back {
    top: 511px;
    background: var(--paper);
  }
  .brand {
    position: absolute;
    left: 0;
    right: 0;
    top: 125px;
    display: flex;
    flex-direction: column;
    align-items: center;
    color: var(--paper);
  }
  .brand__dot {
    width: 130px;
    height: 130px;
    border-radius: 50%;
    background: var(--paper);
    margin-bottom: 38px;
  }
  .brand__name {
    font-size: 44px;
    font-weight: 400;
    letter-spacing: 1px;
    line-height: 1;
  }
  .back-art {
    position: absolute;
    inset: 0;
  }
  .contact {
    position: absolute;
    left: 14px;
    top: 180px;
    color: var(--sky);
  }
  .contact__name {
    margin: 0;
    font-size: 35px;
    font-weight: 700;
    line-height: 1;
  }
  .contact__role {
    margin: 14px 0 0;
    font-size: 23px;
    font-weight: 400;
    letter-spacing: 0.5px;
  }
  .contact__list {
    list-style: none;
    margin: 52px 0 0;
    padding: 0;
    font-size: 24px;
    line-height: 30px;
  }
  .contact__item {
    display: flex;
    align-items: flex-start;
    gap: 10px;
    margin-bottom: 10px;
  }
  .contact__icon {
    width: 30px;
    height: 30px;
    flex: none;
  }
</style>
</head>
<body>
<main class="canvas">
  <section class="card card--front" aria-label="Card front">
    <div class="brand">
      <div class="brand__dot"></div>
      <div class="brand__name">Openbreath Harmony</div>
    </div>
  </section>

  <section class="card card--back" aria-label="Card back">
    <svg class="back-art" viewBox="0 0 745 459" width="745" height="459" aria-hidden="true">
      <path d="M504,0 C510,110 672,190 672,290 C672,380 640,440 600,459 L745,459 L745,0 Z" fill="var(--mist)"/>
      <circle cx="494" cy="285" r="150" fill="none" stroke="var(--sky)" stroke-width="40"/>
    </svg>

    <div class="contact">
      <h1 class="contact__name">Maren Tollefsen</h1>
      <p class="contact__role">DIRECTOR</p>
      <ul class="contact__list">
        <li class="contact__item">
          <svg class="contact__icon" viewBox="0 0 30 30" aria-hidden="true">
            <rect x="1.5" y="7" width="27" height="18" fill="none" stroke="var(--sky)" stroke-width="2"/>
            <path d="M1.5,7 L15,18 L28.5,7 M1.5,25 L11,15 M28.5,25 L19,15" fill="none" stroke="var(--sky)" stroke-width="2"/>
          </svg>
          <span>42 Quillfern Avenue,<br>Dunmorrow QLD 4518</span>
        </li>
        <li class="contact__item">
          <svg class="contact__icon" viewBox="0 0 30 30" aria-hidden="true">
            <circle cx="15" cy="15" r="13.5" fill="none" stroke="var(--sky)" stroke-width="2"/>
            <path d="M10,8 L12.5,8 L13.5,12 L12,13.5 C13,16 14,17 16.5,18 L18,16.5 L22,17.5 L22,20 C22,21 21,22 19.5,22 C13,21.5 8.5,17 8,10.5 C8,9 9,8 10,8 Z" fill="var(--sky)"/>
          </svg>
          <span>0451 628 904</span>
        </li>
      </ul>
    </div>
  </section>
</main>
</body>
</html>
```